Website for Ledger Prowl a cyrpto Mining company that sells crypto mining rigs

β€œIn the age of de-centralised financial services, individuals with a relatively small investment can use their own hardware to process crypto transactions and earn a substantial second income.”

Ledger Prowl provide a personal home and hosted mining solutions to enable individuals to earn monthly crypto currencies of today and the future.”
Home/Products/About
Images – I had assumed this was part of the Design? For the home page I have a 10 second video of blockchain. I can only find on Framevault For any text or sections please refer to our old website www.thirdotter.ae
https://www.framevault.example/video/clip-2741905316-block-chain-concept---consists-network-connections I can buy and send?
On each page I will have a video similar, can you just put placeholder images and videos. I can replace. I am pretty good with Wordpress.
Updates

Please use text from my old website www.thirdottermining.example

Target Market(s)

High Net wealth interested in Crypto

Industry/Entity Type

Crypto Mining

Coding

Coded - Design and coding required

Number of Pages Required

5+ page

Font styles to use
Other font styles liked:
• Sansation

Colors
0054AA
0677BA
7BADD7
CADEEF
E8F1F8

Requirements
Must have
• Video as banner (Will supply Video), Wordpress
Nice to have
• Will need Member login and Shop in future, please ensure this will be possible. (But not part of this project)

```html
<!DOCTYPE html>
<html lang="en">
<head>
<meta charset="utf-8">
<title>Ledger Prowl – Third Otter Mining</title>
<link rel="stylesheet" href="https://fonts.googleapis.com/css2?family=Exo+2:ital,wght@0,400;0,500;0,600;0,700;1,400&display=swap">
<style>
:root{
  --blue:#0054AA;
  --blue-mid:#0677BA;
  --blue-light:#7BADD7;
  --blue-pale:#CADEEF;
  --blue-wash:#E8F1F8;
  --ink:#111111;
  --grey:#8a8f96;
  --field:#f6f8fa;
  --navy:#0b1f4a;
  --white:#ffffff;
}
*{box-sizing:border-box;margin:0;padding:0}
html,body{width:1200px;height:3754px;overflow:hidden}
body{position:relative;background:var(--white);font-family:"Exo 2",sans-serif;color:var(--ink)}
.abs{position:absolute}
.center{text-align:center;left:0;width:1200px}

/* header */
.site-header{top:0;left:0;width:1200px;height:87px;background:var(--white)}
.brand{display:flex;align-items:center;gap:12px;font-weight:600;color:var(--blue-mid);font-size:30px;letter-spacing:1px}
.brand-mark{width:34px;height:34px;border:3px solid var(--blue-mid);border-radius:50%}
.main-nav a{position:absolute;top:36px;font-size:14px;color:var(--ink);text-decoration:none}
.main-nav a.active{color:var(--blue);text-decoration:underline}
.btn-solid{background:var(--blue);color:var(--white);font-size:14px;font-weight:600;display:flex;align-items:center;justify-content:center;border-radius:2px}
.btn-outline{border:1px solid var(--blue);color:var(--blue);font-size:13px;display:flex;align-items:center;justify-content:center;border-radius:2px;background:transparent}

/* hero */
.hero{top:87px;left:0;width:1200px;height:482px;background:
  radial-gradient(ellipse 240px 200px at 250px 240px,rgba(40,220,255,.55),transparent 70%),
  radial-gradient(ellipse 260px 300px at 1060px 220px,rgba(40,190,255,.7),transparent 70%),
  radial-gradient(ellipse 80px 200px at 20px 260px,rgba(40,220,255,.4),transparent 70%),
  linear-gradient(90deg,#121a44,#1d2257 50%,#141a45)}
.play{left:570px;top:302px;width:60px;height:60px;background:rgba(255,255,255,.45);display:flex;align-items:center;justify-content:center}

/* intro */
.section-title{font-weight:600;color:var(--blue);font-size:32px}
.intro-text{font-size:13.5px;line-height:21px}

/* products */
.products{top:894px;left:0;width:1200px;height:619px;background:
  radial-gradient(ellipse 500px 300px at 600px 280px,rgba(20,40,70,.7),transparent 70%),
  linear-gradient(180deg,#05080d,#0c121b 50%,#05070b)}
.products .section-title{color:var(--white)}
.product-card{width:293px;height:150px;background:rgba(10,35,80,.55);display:flex;flex-direction:column;align-items:center}
.product-card.is-active{background:#0a3d86}
.product-icon{margin-top:32px;width:52px;height:52px;background:var(--blue);display:flex;align-items:center;justify-content:center}
.product-name{margin-top:18px;color:var(--white);font-weight:600;font-size:17px}

/* about */
.circuit{top:1513px;left:0;width:1200px;height:547px;background:
  radial-gradient(ellipse 320px 260px at 600px 220px,rgba(60,230,240,.35),transparent 70%),
  radial-gradient(ellipse 300px 300px at 1150px 120px,rgba(60,230,220,.45),transparent 70%),
  linear-gradient(120deg,#0a2a33,#0c3a44 40%,#0a2d3a 70%,#135a68)}
.about-card{left:147px;top:1891px;width:904px;height:419px;background:var(--white);box-shadow:0 2px 14px rgba(0,0,0,.08)}
.team-photo{top:2098px;width:224px;height:252px}
.team-name{top:2362px;width:224px;text-align:center;font-size:15px;font-weight:500}
.team-name.is-active{color:var(--blue)}
.team-overlay{background:linear-gradient(160deg,#2a2a2a,#111);color:var(--white);font-size:12px;line-height:16px;text-align:center;display:flex;align-items:center;padding:0 26px}

/* testimonials */
.testimonials{top:2458px;left:0;width:1200px;height:424px;background:
  radial-gradient(ellipse 500px 220px at 600px 200px,rgba(20,60,130,.5),transparent 70%),
  linear-gradient(180deg,#0a1d45,#0c2352)}
.quote-text{font-size:12.5px;line-height:18px;color:var(--white)}
.dot{width:9px;height:9px;border-radius:50%;border:1px solid var(--blue-light)}

/* contact */
.field{left:617px;width:406px;background:var(--field);font-size:10px;color:var(--grey);padding:16px 15px;box-shadow:0 1px 3px rgba(0,0,0,.05)}

/* footer */
.site-footer{top:3338px;left:0;width:1200px;height:369px;background:
  radial-gradient(ellipse 400px 200px at 600px 100px,rgba(20,70,80,.5),transparent 70%),
  linear-gradient(180deg,#061a20,#072026)}
.contact-box{left:208px;top:3477px;width:783px;height:138px;background:rgba(3,14,18,.75)}
.info-icon{width:38px;height:38px;background:#0a1418;border:1px solid #1f2c30;display:flex;align-items:center;justify-content:center}
.info-label{font-size:11px;color:var(--blue-mid)}
.info-value{font-size:13px;color:var(--white);font-weight:500}
.footer-nav a{position:absolute;top:3656px;font-size:13px;color:var(--white);text-decoration:none}
.footer-nav a.active{color:var(--blue-mid);text-decoration:underline}
.bottom-bar{top:3707px;left:0;width:1200px;height:47px;background:var(--blue)}
.social{top:3718px;width:26px;height:26px;border:1px solid rgba(255,255,255,.7);background:transparent}
</style>
</head>
<body>

<!-- Header -->
<header class="abs site-header">
  <div class="abs brand" style="left:87px;top:24px;"><span class="brand-mark"></span>Ledger Prowl</div>
  <nav class="main-nav">
    <a class="active" href="#" style="left:626px;">Home</a>
    <a href="#" style="left:703px;">Products</a>
    <a href="#" style="left:798px;">FAQ</a>
    <a href="#" style="left:866px;">Contact Us</a>
  </nav>
  <a class="abs btn-solid" href="#" style="left:977px;top:26px;width:135px;height:37px;text-decoration:none;">Get In Touch</a>
</header>

<!-- Hero video -->
<section class="abs hero" role="img" aria-label="Banner video placeholder: blockchain concept, glowing cyan data cubes joined by a chain"></section>
<div class="abs play"><svg width="24" height="26" viewBox="0 0 24 26"><path d="M2 1 L22 13 L2 25 Z" fill="#1e5fb0"/></svg></div>

<!-- Intro -->
<h1 class="abs center section-title" style="top:632px;">Third Otter Mining</h1>
<p class="abs center intro-text" style="top:692px;font-weight:600;">The early bird gets the worm, but the Third Otter gets the cheese.</p>
<p class="abs center intro-text" style="top:713px;">In the age of de-centralised financial services, individuals with a relatively small investment can use their own hardware to<br>process crypto transactions and earn a substantial second income.</p>
<a class="abs btn-outline" href="#" style="left:541px;top:780px;width:118px;height:33px;text-decoration:none;">Read More</a>

<!-- Products -->
<section class="abs products">
  <h2 class="abs center section-title" style="top:63px;font-size:31px;">Our Products</h2>

  <div class="abs product-card" style="left:128px;top:141px;">
    <div class="product-icon"><svg width="26" height="26" viewBox="0 0 26 26"><rect x="6" y="6" width="14" height="14" fill="none" stroke="#fff" stroke-width="2.5"/><path d="M9 2v4M13 2v4M17 2v4M9 20v4M13 20v4M17 20v4" stroke="#fff" stroke-width="2"/></svg></div>
    <div class="product-name">Hardware Installation</div>
  </div>
  <div class="abs product-card" style="left:453px;top:141px;">
    <div class="product-icon"><svg width="26" height="26" viewBox="0 0 26 26"><path d="M4 22 L16 10" stroke="#fff" stroke-width="3"/><path d="M10 4 Q18 4 22 12 L18 14 Q16 9 12 8 Z" fill="#fff"/></svg></div>
    <div class="product-name">Currency Mining</div>
  </div>
  <div class="abs product-card" style="left:778px;top:141px;">
    <div class="product-icon"><svg width="26" height="26" viewBox="0 0 26 26"><rect x="3" y="14" width="5" height="9" fill="#fff"/><rect x="10.5" y="9" width="5" height="14" fill="#fff"/><rect x="18" y="3" width="5" height="20" fill="#fff"/></svg></div>
    <div class="product-name">Crypto Earnings</div>
  </div>

  <div class="abs product-card" style="left:128px;top:316px;">
    <div class="product-icon"><svg width="26" height="26" viewBox="0 0 26 26"><circle cx="15" cy="9" r="7" fill="none" stroke="#fff" stroke-width="2.5"/><path d="M2 16h5l6 4h8v3H12l-5-3H2z" fill="#fff"/></svg></div>
    <div class="product-name">Earn Crypto Every Month</div>
  </div>
  <div class="abs product-card" style="left:453px;top:316px;">
    <div class="product-icon"><svg width="26" height="26" viewBox="0 0 26 26"><circle cx="13" cy="13" r="8" fill="none" stroke="#fff" stroke-width="4" stroke-dasharray="4 2.3"/><circle cx="13" cy="13" r="3.5" fill="#fff"/></svg></div>
    <div class="product-name">Service &amp; Maintenance</div>
  </div>
  <div class="abs product-card is-active" style="left:778px;top:316px;">
    <div class="product-icon"><svg width="26" height="26" viewBox="0 0 26 26"><path d="M13 24V8M13 3l-4 5h8zM13 14L5 10M13 14l8-4" stroke="#fff" stroke-width="2.2" fill="#fff"/></svg></div>
    <div class="product-name">Flexible Mining</div>
  </div>

  <a class="abs btn-outline" href="#" style="left:523px;top:505px;width:153px;height:34px;text-decoration:none;font-size:12px;">Contact Us Today</a>
</section>

<!-- About -->
<div class="abs circuit" role="img" aria-label="Illustration placeholder: glowing teal crypto gem over a circuit board"></div>
<section class="abs about-card"></section>
<h2 class="abs center section-title" style="top:1936px;">About Third Otter Mining</h2>
<p class="abs center" style="top:1981px;font-size:13.5px;font-style:italic;">IT and Operations since 2000, Digital ayments since 2007, Crypto since 2012.</p>
<a class="abs btn-outline" href="#" style="left:541px;top:2016px;width:118px;height:32px;text-decoration:none;">Read More</a>

<div class="abs team-photo" style="left:240px;background:linear-gradient(160deg,#8d8a84,#3a3633 60%,#1c1b1a);" role="img" aria-label="Team portrait of Martin Hale"></div>
<div class="abs team-photo" style="left:496px;background:linear-gradient(180deg,#f3f3f1,#e3e2df 60%,#f6f6f5);" role="img" aria-label="Team portrait of Owen Tarrant"></div>
<div class="abs team-photo team-overlay" style="left:752px;" role="img" aria-label="Operations team working on mining rigs">Our Technology and Operations gurus who track the crypto markets daily. Their remote access to the Third Otter rigs ensure they are optimised.</div>
<div class="abs team-name" style="left:240px;">Martin Hale</div>
<div class="abs team-name" style="left:496px;">Owen Tarrant</div>
<div class="abs team-name is-active" style="left:752px;">Pavel &amp; Dimo Restova</div>

<!-- Testimonials -->
<section class="abs testimonials">
  <h2 class="abs center section-title" style="top:74px;font-size:30px;color:var(--blue);">Testimonials</h2>
  <div class="abs" style="left:571px;top:137px;width:58px;height:54px;background:var(--blue);display:flex;align-items:center;justify-content:center;">
    <svg width="30" height="24" viewBox="0 0 30 24"><path d="M2 12 Q2 3 11 1 L12 4 Q7 6 7 10 H12 V22 H2Z M17 12 Q17 3 26 1 L27 4 Q22 6 22 10 H27 V22 H17Z" fill="#fff"/></svg>
  </div>
  <p class="abs center quote-text" style="top:209px;">I had 10 thousands pounds saved but going nowhere. Owen explained that could buy a mining rig so I decided to invest it in the hardware.<br>He came around himself, took about 2 hours to set it up, showed me how to open a CoinHarbor account and how to check the daily perfor-<br>mance on my mobile or laptop.&nbsp; I can't quite believe it's making me money for what looks like nothing.</p>
  <p class="abs center" style="top:280px;font-size:12px;color:var(--blue-mid);">Office Manager&nbsp;&nbsp;|&nbsp;&nbsp;Harbour Business</p>
  <div class="abs dot" style="left:577px;top:333px;"></div>
  <div class="abs dot" style="left:595px;top:333px;background:var(--blue-mid);border-color:var(--blue-mid);"></div>
  <div class="abs dot" style="left:613px;top:333px;"></div>
</section>

<!-- Contact -->
<section>
  <h2 class="abs" style="left:136px;top:2958px;font-size:30px;font-weight:500;">Ledger Prowl</h2>
  <p class="abs" style="left:136px;top:2999px;font-size:13px;line-height:18px;color:var(--grey);">Lorem Ipsum is simply dummy text of the printing<br>and typesetting industry..</p>
  <svg class="abs" style="left:136px;top:3090px;" width="146" height="162" viewBox="0 0 146 162">
    <path d="M120 60 V20 Q120 6 106 6 H20 Q6 6 6 20 V142 Q6 156 20 156 H70" fill="none" stroke="#dfe1e4" stroke-width="10" stroke-linecap="round"/>
    <path d="M30 44 H96 M30 70 H96 M30 96 H70" stroke="#dfe1e4" stroke-width="10" stroke-linecap="round"/>
    <path d="M74 150 L82 124 L126 80 L142 96 L98 140 Z" fill="none" stroke="#dfe1e4" stroke-width="9" stroke-linejoin="round"/>
  </svg>

  <div class="abs field" style="top:2962px;height:45px;">Full Name</div>
  <div class="abs field" style="top:3015px;height:41px;padding-top:14px;">Email*</div>
  <div class="abs field" style="top:3068px;height:42px;padding-top:15px;">Phone</div>
  <div class="abs field" style="top:3121px;height:87px;">Have questions? We have answers!*</div>
  <a class="abs btn-solid" href="#" style="left:617px;top:3220px;width:112px;height:35px;text-decoration:none;font-size:13px;">Submit</a>
</section>

<!-- Footer -->
<footer class="abs site-footer"></footer>
<div class="abs brand" style="left:500px;top:3395px;font-size:32px;"><span class="brand-mark" style="width:36px;height:36px;"></span>Ledger Prowl</div>
<div class="abs contact-box"></div>
<p class="abs center" style="top:3505px;font-size:15px;font-weight:500;color:var(--white);">CONTACT INFO</p>

<div class="abs info-icon" style="left:249px;top:3552px;"><svg width="14" height="18" viewBox="0 0 14 18"><path d="M7 1a6 6 0 0 1 6 6c0 4-6 10-6 10S1 11 1 7a6 6 0 0 1 6-6z" fill="#fff"/><circle cx="7" cy="7" r="2.2" fill="#0a1418"/></svg></div>
<div class="abs" style="left:304px;top:3553px;"><div class="info-label">Address</div><div class="info-value">Harbour Quarter, Lumen City</div></div>

<div class="abs info-icon" style="left:547px;top:3552px;"><svg width="16" height="12" viewBox="0 0 16 12"><rect width="16" height="12" fill="#fff"/><path d="M0 0 L8 7 L16 0" fill="none" stroke="#0a1418" stroke-width="1.5"/></svg></div>
<div class="abs" style="left:602px;top:3553px;"><div class="info-label">Email</div><div class="info-value">owen@ledgerprowl.example</div></div>

<div class="abs info-icon" style="left:783px;top:3552px;"><svg width="14" height="14" viewBox="0 0 14 14"><path d="M3 0 L6 4 L4 6 Q6 9 8 10 L10 8 L14 11 L12 14 Q4 13 0 3 Z" fill="#fff"/></svg></div>
<div class="abs" style="left:838px;top:3553px;"><div class="info-label">Phone</div><div class="info-value">+971 50 000 1234</div></div>

<nav class="footer-nav">
  <a class="active" href="#" style="left:455px;">Home</a>
  <a href="#" style="left:527px;">Products</a>
  <a href="#" style="left:617px;">FAQ</a>
  <a href="#" style="left:680px;">Contact Us</a>
</nav>

<div class="abs bottom-bar"></div>
<p class="abs" style="left:88px;top:3723px;font-size:12px;color:var(--white);">Copyright © 2021 Ledger Prowl Solutions LLC. All Rights Reserved, Business License Number 4470192</p>
<div class="abs social" style="left:1009px;"></div>
<div class="abs social" style="left:1047px;"></div>
<div class="abs social" style="left:1085px;"></div>

</body>
</html>
```